Web Design Services Create a Similar website to my Competitor

We would like a similar website designed like our main competitor with all the features there website has and more. Also we would like to accept payments through our website and to rank quickly with seo based on our home page and other page use of high traffic keywords. this is the website we would like to have ours designed similar to https://www.festivalpaintbay.com. we will be providing the same services and more just at a different location. We would also like to know be able to easily make adjustments to the website when its time to edit it please thanks.

Basically I am looking to have have similar website built almost exactly the same but with my logo, and other personalized information to my company Orla Maskrade Beauty Lounge. I will need to send you model images and logo design idea but the body and user interface of my competitor https://www.festivalpaintbay.com will be exactly the same. I can be reached anytime to answer any questions you may have.
Updates

Hi Designers I would like to clarify some information Festival Paint Bay is my Competitor we are not affiliated. I would like my website to be designed similar to hers but please do not take any content from her website to put on mine I will be providing images to be posted on my website. Also please do not use any of her videos or ClipTube videos on my website to avoid any legal issues. Thanks for your understanding.

Target Market(s)

Make up Application Services For Events and Trinidad and Tobago Carnival

Industry/Entity Type

Beauty and Makeup Application and services

Coding

Coded - Design and coding required

Number of Pages Required

5+ page

Font styles to use
Sans Serif

Colors
E54698
E96AAD
F1A4CE
F9D9EA
FCEFF6
A7469A
B969AE
D3A5CF
EDDBEB
F8F0F9

Requirements
Must have
• Must be similar to my competitor, need a video section, testimonial and must be easily able to navigate to information sections and book now payment notifications running on all pages so customers can easily book there spot for 2026 carnival
Nice to have
• I am looking to have a similar website to https://www.festivalpaintbay.com created but make it as minimal and modern
Should not have
• Project can be coded if it makes it easier to create a similar look to my competitor just ask that updates can easily be made later on.

```html
<!DOCTYPE html>
<html lang="en">
<head>
<meta charset="utf-8">
<title>Orla Maskrade Beauty Lounge</title>
<link href="https://fonts.googleapis.com/css2?family=Oswald:wght@500;600;700&family=Poppins:wght@400;500;600&display=swap" rel="stylesheet">
<style>
:root{
  --pink:#E54698;--pink-2:#E96AAD;--pink-3:#F1A4CE;--pink-4:#F9D9EA;--pink-5:#FCEFF6;
  --purple:#A7469A;--purple-2:#B969AE;--purple-3:#D3A5CF;--purple-4:#EDDBEB;--purple-5:#F8F0F9;
  --ink:#2a2a2a;--dark:#1c0a16;--white:#fff;
}
*{box-sizing:border-box;margin:0;padding:0}
html,body{width:1200px;height:4796px;overflow:hidden}
body{font-family:'Poppins',sans-serif;color:var(--ink);background:var(--white);position:relative}
.abs{position:absolute}
.display{font-family:'Oswald',sans-serif;font-weight:700;text-transform:uppercase;letter-spacing:-.5px}
.btn{position:absolute;display:flex;align-items:center;justify-content:center;font-size:11px;font-weight:600;text-transform:uppercase;letter-spacing:.5px;border-radius:4px}
.btn-pink{background:linear-gradient(90deg,var(--pink),var(--purple));color:#fff}
.btn-white{background:#fff;color:var(--pink)}
.arrow{position:absolute;width:30px;height:30px;border:1.5px solid var(--purple-3);border-radius:50%;display:flex;align-items:center;justify-content:center}
.ph{position:absolute}
/* header */
.site-header{position:absolute;top:0;left:0;width:1200px;height:52px;background:#fff}
.brand{position:absolute;left:120px;top:14px;font-family:'Oswald',sans-serif;font-weight:600;font-size:19px;color:var(--pink)}
.nav{position:absolute;top:20px;left:584px;display:flex;gap:30px;font-size:11px;font-weight:500}
.nav .active{color:var(--pink)}
/* hero */
.hero{position:absolute;top:52px;left:0;width:1200px;height:568px;background:linear-gradient(180deg,#e2711a 0%,#c2371a 40%,#7a2a3a 75%,#4a2a4a 100%)}
.hero h1{position:absolute;top:283px;width:100%;text-align:center;color:#fff;font-family:'Oswald',sans-serif;font-weight:600;font-size:48px;line-height:55px}
.hero h1 span{color:var(--pink-2)}
.hero p{position:absolute;top:398px;left:340px;width:520px;text-align:center;color:#fff;font-size:11.5px;line-height:20px}
/* about */
.about-title{left:688px;top:730px;font-size:32px;color:var(--pink)}
.about-copy{left:686px;top:778px;width:390px;font-size:11px;line-height:17px}
.about-copy p+p{margin-top:17px}
.outline-word{left:0;top:1060px;width:1200px;white-space:nowrap;font-family:'Oswald',sans-serif;font-weight:700;font-size:108px;color:transparent;-webkit-text-stroke:1.5px var(--purple-4);text-transform:uppercase;letter-spacing:1px}
/* services */
.services{position:absolute;top:1162px;left:0;width:1200px;height:503px;background:linear-gradient(180deg,var(--purple-4),var(--purple-3))}
.section-title{position:absolute;width:1200px;left:0;text-align:center;font-size:31px}
.card{position:absolute;top:1287px;width:223px;height:235px;background:#fff}
.card .ph{left:0;top:0;width:223px;height:188px}
.card .label{position:absolute;left:14px;top:204px;font-family:'Oswald',sans-serif;font-weight:500;font-size:12.5px;color:var(--pink);text-transform:uppercase}
.card .go{position:absolute;right:14px;top:202px;width:20px;height:20px;border-radius:50%;background:var(--pink);display:flex;align-items:center;justify-content:center}
/* gallery */
.tile{position:absolute;width:305px;height:200px}
/* banners */
.pkg{position:absolute;top:2266px;left:0;width:1200px;height:269px;background:linear-gradient(90deg,var(--purple),var(--pink) 50%,var(--purple))}
.pkg h2,.cta h2{position:absolute;width:100%;text-align:center;color:#fff}
.pkg p,.cta p{position:absolute;width:100%;text-align:center;color:#fff;font-size:11px;line-height:17px}
/* testimonials */
.quote-card{position:absolute;background:#fff;border:1px solid var(--pink-4);box-shadow:0 4px 18px rgba(167,70,154,.15);text-align:center}
.qmark{font-family:'Oswald',sans-serif;font-weight:700;color:var(--pink);font-size:72px;line-height:60px}
.quote-text{font-size:14px;line-height:19px;color:#333}
.quote-name{font-family:'Oswald',sans-serif;font-weight:500;font-size:13px;margin-top:14px}
.stars{color:#f4b400;font-size:18px;letter-spacing:1px}
/* behind */
.behind{position:absolute;top:3017px;left:0;width:1200px;height:378px;background:linear-gradient(90deg,#7e2f7e,var(--purple) 50%,#8e3a86)}
/* faq */
.faq-row{position:absolute;left:205px;width:795px;border:1.5px solid var(--purple-3);background:#fff;display:flex}
.faq-num{width:88px;border-right:1.5px solid var(--purple-3);display:flex;align-items:center;justify-content:center;font-family:'Oswald',sans-serif;font-size:26px;font-weight:500}
.faq-q{padding:0 16px;display:flex;flex-direction:column;justify-content:center;font-size:15px;font-family:'Oswald',sans-serif;font-weight:400}
.faq-q small{font-size:9px;margin-top:6px;font-family:'Poppins',sans-serif}
.faq-open .faq-num{background:var(--purple-3)}
/* cta */
.cta{position:absolute;top:4256px;left:0;width:1200px;height:251px;background:linear-gradient(90deg,#8a2f8a,var(--pink) 45%,#c83a55)}
/* footer */
.footer{position:absolute;top:4507px;left:0;width:1200px;height:289px;background:var(--dark);color:#fff}
.f-head{position:absolute;top:64px;font-size:11px;font-weight:600;text-transform:uppercase}
.f-list{position:absolute;top:96px;font-size:9.5px;line-height:24px;text-transform:uppercase}
.f-item{display:flex;align-items:center;gap:8px;font-size:9.5px;line-height:12px;margin-bottom:12px}
.f-ico{width:22px;height:22px;border:1px solid var(--pink);border-radius:3px;display:flex;align-items:center;justify-content:center;flex:none}
</style>
</head>
<body>

<header class="site-header">
  <div class="brand">Orla Maskrade Beauty Lounge</div>
  <nav class="nav"><span class="active">HOME</span><span>ABOUT US</span><span>SERVICES</span><span>PACKAGES</span><span>FAQS</span></nav>
  <div class="btn btn-pink" style="left:968px;top:9px;width:110px;height:34px;font-size:10px">Contact Us</div>
</header>

<section class="hero" role="img" aria-label="Carnival performer in a golden headpiece with orange and red feathers">
  <h1>Get Carnival-Ready with <span>Orla<br>Maskrade</span> Beauty Lounge</h1>
  <p>Your one-stop glam destination for stunning Carnival makeup, flawless beauty looks, and unforgettable vibes. Serving [Your City or Country].</p>
  <div class="btn btn-pink" style="left:508px;top:454px;width:196px;height:48px">Book Your Glam Now</div>
</section>

<section class="about">
  <div class="abs" style="left:120px;top:683px;width:330px;height:347px;background:var(--pink)"></div>
  <div class="ph" role="img" aria-label="Model in yellow feather carnival headdress" style="left:135px;top:697px;width:317px;height:333px;background:linear-gradient(160deg,#e8c22a,#c8503a 60%,#8a2b3f)"></div>
  <div class="ph" role="img" aria-label="Carnival costume in blue and orange plumes" style="left:358px;top:752px;width:198px;height:218px;border:4px solid #fff;background:linear-gradient(180deg,#1e3a6a,#2a2a3a 60%,#5a3a2a);box-shadow:0 0 0 1px #222"></div>
  <h2 class="abs display about-title">About Orla</h2>
  <div class="abs about-copy">
    <p>At Orla Maskrade Beauty Lounge, we specialize in bold, vibrant, and flawless makeup looks for Carnival, festivals, photoshoots, and all your special events. Whether you're preparing for the road or the stage, we're here to help you feel powerful, radiant, and confident.</p>
    <p>With top-tier products, trained artists, and a passion for Caribbean culture and beauty, we bring the glam to you. Located in [Your Location], our mission is to make every client feel like royalty.</p>
  </div>
  <div class="btn btn-pink" style="left:685px;top:944px;width:158px;height:50px;font-size:10px">Meet Our Artists</div>
  <div class="abs outline-word">Orla Maskrade Beauty Lounge.</div>
</section>

<section class="services">
  <h2 class="display section-title" style="top:52px;color:var(--pink)">Our Glam Services</h2>
</section>
<div class="arrow" style="left:68px;top:1391px"><svg width="10" height="10" viewBox="0 0 10 10"><path d="M6 1 2 5l4 4" fill="none" stroke="#A7469A" stroke-width="1.4"/></svg></div>
<div class="arrow" style="left:1100px;top:1391px"><svg width="10" height="10" viewBox="0 0 10 10"><path d="M4 1l4 4-4 4" fill="none" stroke="#A7469A" stroke-width="1.4"/></svg></div>
<div class="card" style="left:122px"><div class="ph" role="img" aria-label="Rainbow carnival eye makeup" style="background:linear-gradient(135deg,#3a7ad8,#e0b030 50%,#d83a8a)"></div><div class="label">Carnival Full Glam</div><div class="go"><svg width="8" height="8" viewBox="0 0 8 8"><path d="M2 6l4-4M3 2h3v3" stroke="#fff" fill="none"/></svg></div></div>
<div class="card" style="left:366px"><div class="ph" role="img" aria-label="Dancer with pink feathered fan" style="background:linear-gradient(135deg,#c83aa8,#e882c8 55%,#f0d0e0)"></div><div class="label">Soft Glam / Natural Beat</div><div class="go"><svg width="8" height="8" viewBox="0 0 8 8"><path d="M2 6l4-4M3 2h3v3" stroke="#fff" fill="none"/></svg></div></div>
<div class="card" style="left:610px"><div class="ph" role="img" aria-label="Festival fantasy face gems look" style="background:linear-gradient(135deg,#6a4a3a,#e0c0a0 50%,#5a9ad0)"></div><div class="label">Festival Fantasy Looks</div><div class="go"><svg width="8" height="8" viewBox="0 0 8 8"><path d="M2 6l4-4M3 2h3v3" stroke="#fff" fill="none"/></svg></div></div>
<div class="card" style="left:853px"><div class="ph" role="img" aria-label="Group of carnival performers in feathers" style="background:linear-gradient(135deg,#d83a5a,#8a3aa8 50%,#e83a9a)"></div><div class="label">Group Glam Packages</div><div class="go"><svg width="8" height="8" viewBox="0 0 8 8"><path d="M2 6l4-4M3 2h3v3" stroke="#fff" fill="none"/></svg></div></div>
<div class="btn btn-pink" style="left:517px;top:1555px;width:166px;height:50px;font-size:10px">View All Services</div>

<section class="gallery">
  <h2 class="display section-title" style="top:1720px;color:var(--purple)">Image Gallery</h2>
  <div class="arrow" style="left:68px;top:1990px"><svg width="10" height="10" viewBox="0 0 10 10"><path d="M6 1 2 5l4 4" fill="none" stroke="#A7469A" stroke-width="1.4"/></svg></div>
  <div class="arrow" style="left:1100px;top:1990px"><svg width="10" height="10" viewBox="0 0 10 10"><path d="M4 1l4 4-4 4" fill="none" stroke="#A7469A" stroke-width="1.4"/></svg></div>
  <div class="tile" role="img" aria-label="Red masquerade mask portrait" style="left:122px;top:1792px;background:linear-gradient(135deg,#8a1a1a,#d02a2a 50%,#3a0a0a)"></div>
  <div class="tile" role="img" aria-label="Costumed model among city towers" style="left:447px;top:1792px;background:linear-gradient(180deg,#b0a8a0,#6a6a7a 60%,#3a3a4a)"></div>
  <div class="tile" role="img" aria-label="Green feathered masquerade mask" style="left:772px;top:1792px;background:linear-gradient(135deg,#1a4a4a,#2a8a7a 50%,#a07a2a)"></div>
  <div class="tile" role="img" aria-label="Purple feather costume portrait" style="left:122px;top:2003px;background:linear-gradient(135deg,#5a1a8a,#c02ab0 50%,#e05aa0)"></div>
  <div class="tile" role="img" aria-label="Red and white carnival mask with confetti" style="left:447px;top:2003px;background:linear-gradient(135deg,#1a1a1a,#c82a2a 50%,#2a2a2a)"></div>
  <div class="tile" role="img" aria-label="Carnival band on parade in yellow feathers" style="left:772px;top:2003px;background:linear-gradient(135deg,#3a4a2a,#e0c02a 50%,#c83a8a)"></div>
</section>

<section class="pkg">
  <h2 class="display" style="top:60px;font-size:29px">Get Road-Ready with Our 2025 Carnival Glam Packages!</h2>
  <p style="top:104px;padding:0 310px">Secure your slot for Carnival Season now — appointments fill up fast! Choose from single-session glam, weekend bundles, or full-band team bookings.</p>
  <div class="btn btn-white" style="left:493px;top:160px;width:214px;height:47px">Book Carnival Glam Now</div>
</section>

<section class="testimonials">
  <h2 class="display section-title" style="top:2590px;color:var(--purple)">What Our Clients Say</h2>
  <div class="arrow" style="left:68px;top:2795px"><svg width="10" height="10" viewBox="0 0 10 10"><path d="M6 1 2 5l4 4" fill="none" stroke="#A7469A" stroke-width="1.4"/></svg></div>
  <div class="quote-card" style="left:122px;top:2700px;width:290px;height:226px;padding:30px 20px 0;overflow:hidden;text-align:left">
    <div class="qmark" style="text-align:center;margin-left:40px">“</div>
    <div class="quote-text" style="white-space:nowrap;padding-left:30px">"Orla made me feel like a queen on<br>Monday and Tuesday. The glam held<br>&nbsp;&nbsp;&nbsp;and looked AMAZING in every shot."</div>
    <div class="quote-name" style="padding-left:170px">Marisol T.</div>
    <div style="padding-left:148px;display:flex;align-items:center;gap:6px"><span style="width:13px;height:13px;border-radius:50%;border:2px solid #888;display:inline-block"></span><span class="stars">★★★★★</span></div>
  </div>
  <div class="quote-card" style="left:397px;top:2660px;width:408px;height:300px;padding:28px 22px 0">
    <div class="qmark">“</div>
    <div class="quote-text">"Orla didn't just do my makeup — she gave me an experience. From the glitter to the lashes to the energy in the room, I felt like a true queen on the road. The glam lasted all day, survived the heat, and looked perfect in every photo. I've never felt more confident or beautiful!"</div>
    <div class="quote-name">Marisol T., 2024 Carnival Client</div>
    <div style="display:flex;justify-content:center;align-items:center;gap:6px"><span style="width:13px;height:13px;border-radius:50%;border:2px solid #888;display:inline-block"></span><span class="stars">★★★★★</span></div>
  </div>
  <div class="arrow" style="left:822px;top:2795px"><svg width="10" height="10" viewBox="0 0 10 10"><path d="M4 1l4 4-4 4" fill="none" stroke="#A7469A" stroke-width="1.4"/></svg></div>
  <div class="ph" role="img" aria-label="Smiling woman in gold masquerade mask and red feather headpiece" style="left:860px;top:2590px;width:310px;height:427px;background:radial-gradient(ellipse at 60% 40%,#e85a5a,#d03a4a 35%,#f3d0d8 70%,transparent 72%)"></div>
</section>

<section class="behind">
  <h2 class="display" style="position:absolute;top:70px;width:100%;text-align:center;color:#fff;font-size:31px">Behind the Glam</h2>
  <p style="position:absolute;top:116px;width:100%;text-align:center;color:#fff;font-size:11px;line-height:18px">Watch us work our magic on real clients and get a behind-the-scenes<br>look at what goes into a flawless Carnival glam experience.</p>
</section>
<div class="ph" role="img" aria-label="Video: artists applying makeup to performers at a lit mirror" style="left:122px;top:3203px;width:955px;height:406px;border:3px solid var(--purple-2);background:linear-gradient(90deg,#1a1a2a,#6a4a4a 40%,#c86a3a 65%,#2a2a2a 85%,#eee)"></div>
<div class="abs" style="left:563px;top:3370px;width:74px;height:74px;border-radius:50%;background:rgba(167,70,154,.75);border:2px solid #fff;display:flex;align-items:center;justify-content:center"><svg width="22" height="24" viewBox="0 0 22 24"><path d="M4 2l16 10-16 10z" fill="#fff"/></svg></div>

<section class="faq">
  <h2 class="display section-title" style="top:3668px;color:var(--pink)">Frequently Asked Questions</h2>
  <div class="faq-row" style="top:3742px;height:62px"><div class="faq-num">1</div><div class="faq-q">Do you offer group or band glam bookings?</div></div>
  <div class="faq-row" style="top:3816px;height:62px"><div class="faq-num">2</div><div class="faq-q">How early should I book for Carnival?</div></div>
  <div class="faq-row faq-open" style="top:3890px;height:86px;background:var(--purple-5)"><div class="faq-num">3</div><div class="faq-q">What's included in a Carnival Glam session?<small>From skin prep to lashes and glitter — it's a full glam experience using high-quality, long-lasting products.</small></div></div>
  <div class="faq-row" style="top:3988px;height:62px"><div class="faq-num">4</div><div class="faq-q">How do I pay?</div></div>
  <div class="faq-row" style="top:4062px;height:62px"><div class="faq-num">5</div><div class="faq-q">Can I cancel or reschedule my booking?</div></div>
  <div class="faq-row" style="top:4136px;height:62px"><div class="faq-num">6</div><div class="faq-q">How should I prepare for my appointment?</div></div>
</section>

<section class="cta">
  <h2 style="top:50px;font-family:'Oswald',sans-serif;font-weight:600;font-size:32px">Limited appointments available. Don't wait to secure your spot.</h2>
  <p style="top:100px">Let us bring the glitter, glam, and goddess energy to your Carnival experience.</p>
  <div class="btn btn-white" style="left:509px;top:144px;width:182px;height:50px">Book Your Glam Now</div>
</section>

<footer class="footer">
  <div style="position:absolute;left:120px;top:60px;font-family:'Oswald',sans-serif;font-weight:600;font-size:18px;color:var(--pink)">Orla Maskrade Beauty Lounge</div>
  <p style="position:absolute;left:120px;top:100px;width:235px;font-size:9.5px;line-height:16px">At Orla Maskrade Beauty Lounge, we specialize in bold, vibrant, and flawless makeup looks for Carnival, festivals, photoshoots, and all your special events.</p>
  <div class="f-head" style="left:440px">Quick Links</div>
  <div class="f-list" style="left:440px">Home<br>About Us<br>Services<br>Packages<br>FAQs</div>
  <div class="f-head" style="left:578px">Contact Info</div>
  <div style="position:absolute;left:580px;top:96px;width:160px">
    <div class="f-item"><span class="f-ico"><svg width="11" height="11" viewBox="0 0 12 12"><path d="M3 1l2 3-1 1c1 2 2 3 4 4l1-1 3 2-1 2C6 12 0 6 1 2z" fill="#E54698"/></svg></span>+ 123 456 789</div>
    <div class="f-item"><span class="f-ico"><svg width="12" height="9" viewBox="0 0 12 9"><rect x=".5" y=".5" width="11" height="8" fill="none" stroke="#E54698"/><path d="M1 1l5 4 5-4" fill="none" stroke="#E54698"/></svg></span>Orla Maskrade Beauty Lounge@.com</div>
    <div class="f-item"><span class="f-ico"><svg width="11" height="11" viewBox="0 0 12 12"><circle cx="6" cy="6" r="5" fill="none" stroke="#E54698"/><path d="M1 6h10M6 1v10" stroke="#E54698"/></svg></span>orlamaskradebeauty lounge.com</div>
  </div>
  <div class="f-head" style="left:760px">Follow Us</div>
  <div style="position:absolute;left:762px;top:96px">
    <div class="f-item"><span class="f-ico"></span>FaceSpace</div>
    <div class="f-item"><span class="f-ico"></span>InstaFrame</div>
    <div class="f-item"><span class="f-ico"></span>Chirper</div>
  </div>
  <div class="f-head" style="left:894px">Newsletter Signup</div>
  <div style="position:absolute;left:894px;top:95px;width:183px;height:48px;border:1px solid #777;border-radius:6px;font-size:9.5px;padding:16px 14px;color:#ddd">Email</div>
  <div class="btn btn-pink" style="left:894px;top:155px;width:183px;height:48px;font-size:10px">Subscribe</div>
  <div style="position:absolute;left:120px;top:248px;width:957px;height:1px;background:#555"></div>
  <div style="position:absolute;left:120px;top:259px;font-size:9px">© 2025 Orla Maskrade Beauty Lounge All rights reserved.</div>
  <div style="position:absolute;left:827px;top:259px;font-size:9px;display:flex;gap:14px"><span>Company</span><span>Privacy Policy</span><span>Terms and Conditions</span></div>
</footer>

</body>
</html>
```